General Power Point Presentation Pack

Hello Designers,

I am after a professional looking Microsoft PowerPoint deck that can be used for our corporate presentations. The pack should include a:

Title Page
Tittle and Content Page
Section Header Sheet
Two Content Page
Title Only Page
Blank Page
Content with Caption Page
Picture with Caption Page

I have included my brand guidelines and colours. I have also included some photos you may be able to use. Can you please ensure the pack has page numbering and that when you print it that it can be printed to full A4 Page.

Industry/Entity Type

Property Development & Construction

Requirements
Must have
• Prefer a white or very light coloured background

```html
<!DOCTYPE html>
<html lang="en">
<head>
<meta charset="utf-8">
<title>Northvale Presentation Pack</title>
<link rel="stylesheet" href="https://fonts.googleapis.com/css2?family=Hind:wght@500;600;700&family=Open+Sans:ital,wght@0,400;0,600;1,400&display=swap">
<style>
:root{
  --gold:#cfa66a;
  --gold-soft:rgba(207,166,106,.88);
  --ink:#222222;
  --muted:#b3b3b3;
  --canvas:#c8c8c8;
  --paper:#ffffff;
  --interior-a:#e9e4dc;--interior-b:#b9ab97;
  --exterior-a:#a9a0a8;--exterior-b:#5d5249;
  --facade-a:#b8c4cc;--facade-b:#4e4a42;
}
*{margin:0;padding:0;box-sizing:border-box}
html,body{width:676px;height:1200px;overflow:hidden;background:var(--canvas)}
body{position:relative;font-family:"Open Sans",Arial,sans-serif;color:var(--ink)}
.slide{position:absolute;width:311px;height:175px;background:var(--paper);overflow:hidden}
.accent-bar{position:absolute;left:8.4px;top:0;width:5px;height:22px;background:var(--gold)}
.slide-title{position:absolute;left:20.5px;top:10px;font-family:"Hind",sans-serif;font-weight:700;font-size:9.6px;letter-spacing:.1px}
.brand{position:absolute;right:8px;top:10px;display:flex;align-items:center;gap:2px;font-family:"Hind",sans-serif;font-weight:600;font-size:5.6px;color:var(--gold)}
.brand-mark{width:3.6px;height:3.6px;background:var(--gold)}
.footer-line{position:absolute;left:8.4px;top:167px;width:288px;height:.5px;background:var(--gold)}
.page-no{position:absolute;left:301px;top:163px;width:10px;height:8px;background:var(--gold);color:#fff;font-size:3px;display:flex;align-items:center;justify-content:center}
.body{position:absolute;font-size:4.9px;line-height:6.2px}
.body p{margin-bottom:6.2px}
.body p.tight{margin-bottom:0}
.subhead{color:var(--gold);font-weight:600;border-bottom:.5px solid var(--gold);padding-bottom:2px;margin-bottom:6px}
.photo{position:absolute}
.interior{background:linear-gradient(135deg,var(--interior-a),var(--interior-b))}
.exterior{background:linear-gradient(160deg,var(--exterior-a) 0%,#8a7b74 45%,var(--exterior-b) 100%)}
.facade{background:linear-gradient(100deg,#3f4a3a 0%,var(--facade-b) 25%,#9c9486 55%,var(--facade-a) 100%)}
.tower{background:linear-gradient(180deg,#9fb4c6 0%,#6d6660 55%,#4b4440 100%)}
.caption-line{position:absolute;height:.5px;background:#e4d3b6}
.caption{position:absolute;font-style:italic;font-size:4.9px;color:var(--muted)}

/* title slide */
.cover{left:168px;top:28px}
.cover-photo{left:0;top:9.3px;width:311px;height:156px}
.cover-panel{position:absolute;left:9.3px;top:0;width:143px;height:175px;background:var(--gold-soft)}
.cover-brand{position:absolute;left:9.3px;width:143px;top:46px;text-align:center;font-family:"Hind",sans-serif;font-weight:600;font-size:13px;color:#fff}
.cover-title{position:absolute;left:9.3px;width:143px;top:121px;text-align:center;font-family:"Hind",sans-serif;font-weight:700;font-size:15px;color:#fff}
.cover-rule{position:absolute;left:0;top:148px;width:152px;height:.6px;background:#fff}

/* section header */
.section-band{left:0;top:35px;width:311px;height:99px}
.section-panel{position:absolute;left:33px;top:0;width:68.5px;height:157.5px;background:var(--gold-soft)}
.section-text{position:absolute;left:42px;top:73px;font-family:"Hind",sans-serif;font-weight:700;font-size:11.5px;line-height:13px;color:#fff}

/* blank */
.top-tab{position:absolute;left:8px;top:0;width:34px;height:4.6px;background:var(--gold)}

/* thank you */
.thanks-panel{position:absolute;left:8px;top:0;width:105px;height:175px;background:var(--gold)}
.thanks-text{position:absolute;left:30px;top:62px;font-family:"Hind",sans-serif;font-weight:700;font-size:19px;line-height:22px;color:#fff}
.thanks-brand{position:absolute;left:160px;top:70px;display:flex;align-items:center;gap:4px;font-family:"Hind",sans-serif;font-weight:600;font-size:19px;color:var(--gold)}
.thanks-brand .brand-mark{width:9px;height:9px}
.thanks-line{left:113px;width:183px}
</style>
</head>
<body>

<!-- Title page -->
<section class="slide cover">
  <div class="photo interior cover-photo" role="img" aria-label="Bright apartment living room with sofa, dining table and garden view"></div>
  <div class="cover-panel"></div>
  <div class="cover-rule"></div>
  <div class="cover-brand">Northvale</div>
  <h1 class="cover-title">Title Goes Here</h1>
</section>

<!-- Title and content -->
<section class="slide" style="left:12px;top:220px">
  <div class="accent-bar"></div><h2 class="slide-title">TITLE GOES HERE</h2>
  <div class="brand"><span class="brand-mark"></span>Northvale</div>
  <div class="body" style="left:20.5px;top:29px;width:272px">
    <p>Lorem ipsum dolor sit amet, consectetuer adipiscing elit. Maecenas porttitor congue massa. Fusce posuere, magna sed pulvinar ultricies, purus lectus malesuada libero, sit amet commodo magna eros quis urna.</p>
    <p>Nunc viverra imperdiet enim. Fusce est. Vivamus a tellus.</p>
    <p class="tight">Pellentesque habitant morbi tristique senectus et netus et malesuada fames ac turpis egestas. Proin pharetra nonummy pede. Mauris et orci.</p>
    <p>Lorem ipsum dolor sit amet, consectetuer adipiscing elit. Maecenas porttitor congue massa. Fusce posuere, magna sed pulvinar ultricies, purus lectus malesuada libero, sit amet commodo magna eros quis urna.</p>
    <p class="subhead">Lorem ipsum dolor sit amet</p>
    <p>consectetuer adipiscing elit. Maecenas porttitor congue massa. Fusce posuere, magna sed pulvinar ultricies, purus lectus malesuada libero, sit amet commodo magna eros quis urna.</p>
    <p>Nunc viverra imperdiet enim. Fusce est. Vivamus a tellus.</p>
    <p class="tight">Pellentesque habitant morbi tristique senectus et netus et malesuada fames ac turpis egestas. Proin pharetra nonummy pede. Mauris et orci.</p>
    <p>Lorem ipsum dolor sit amet, consectetuer adipiscing elit. Maecenas porttitor congue massa. Fusce posuere, magna sed</p>
  </div>
  <div class="footer-line"></div><div class="page-no">1</div>
</section>

<!-- Two content -->
<section class="slide" style="left:338px;top:220px">
  <div class="accent-bar"></div><h2 class="slide-title">TITLE GOES HERE</h2>
  <div class="brand"><span class="brand-mark"></span>Northvale</div>
  <div class="body" style="left:20.5px;top:29px;width:100px">
    <p>Lorem ipsum dolor sit amet, consectetuer adipiscing elit. Maecenas porttitor congue massa. Fusce posuere, magna sed pulvinar ultricies, purus lectus malesuada libero, sit amet commodo magna eros quis urna.</p>
    <p>Nunc viverra imperdiet enim. Fusce est. Vivamus a tellus.</p>
    <p class="tight">Pellentesque habitant morbi tristique senectus et netus et malesuada fames ac turpis egestas. Proin pharetra nonummy pede. Mauris et orci.</p>
    <p>Lorem ipsum dolor sit amet, consectetuer adipiscing elit. Maecenas porttitor congue massa. Fusce posuere, magna sed pulvinar ultricies, purus lectus malesuada libero, sit amet commodo magna eros quis urna.</p>
  </div>
  <div class="body" style="left:138px;top:29px;width:156px">
    <p>Lorem ipsum dolor sit amet, consectetuer adipiscing elit. Maecenas porttitor congue massa. Fusce posuere, magna sed pulvinar ultricies, purus lectus malesuada libero, sit amet commodo magna eros quis urna.</p>
    <p>Nunc viverra imperdiet enim. Fusce est. Vivamus a tellus.</p>
    <p class="tight">Pellentesque habitant morbi tristique senectus et netus et malesuada fames ac turpis egestas. Proin pharetra nonummy pede. Mauris et orci.</p>
    <p>Lorem ipsum dolor sit amet, consectetuer adipiscing elit. Maecenas porttitor congue massa. Fusce posuere, magna sed pulvinar ultricies, purus lectus malesuada libero, sit amet commodo magna eros quis urna. Pulvina r ultricies, purus lectus malesuada libero, sit amet commodo magna eros quis urna. pulvinar ultricies, purus lectus malesuada libero, sit amet commodo magna eros quis urna.</p>
  </div>
  <div class="footer-line"></div><div class="page-no">2</div>
</section>

<!-- Content with picture -->
<section class="slide" style="left:12px;top:410px">
  <div class="accent-bar"></div><h2 class="slide-title">TITLE GOES HERE</h2>
  <div class="brand"><span class="brand-mark"></span>Northvale</div>
  <div class="body" style="left:20.5px;top:29px;width:100px">
    <p>Lorem ipsum dolor sit amet, consectetuer adipiscing elit. Maecenas porttitor congue massa. Fusce posuere, magna sed pulvinar ultricies, purus lectus malesuada libero, sit amet commodo magna eros quis urna.</p>
    <p>Nunc viverra imperdiet enim. Fusce est. Vivamus a tellus.</p>
    <p class="tight">Pellentesque habitant morbi tristique senectus et netus et malesuada fames ac turpis egestas. Proin pharetra nonummy pede. Mauris et orci.</p>
    <p>Lorem ipsum dolor sit amet, consectetuer adipiscing elit. Maecenas porttitor congue massa. Fusce posuere, magna sed pulvinar ultricies, purus lectus malesuada libero, sit amet commodo magna eros quis urna.</p>
  </div>
  <div style="position:absolute;left:133px;top:24px;width:18px;height:10px;background:var(--gold)"></div>
  <div class="photo exterior" style="left:136px;top:27.5px;width:175px;height:116.5px" role="img" aria-label="Apartment complex at dusk with palm trees and landscaped entry path"></div>
  <div class="footer-line"></div><div class="page-no">3</div>
</section>

<!-- Section header -->
<section class="slide" style="left:338px;top:410px">
  <div class="brand"><span class="brand-mark"></span>Northvale</div>
  <div class="photo facade section-band" role="img" aria-label="Modern residential facade with balconies and gold screens"></div>
  <div class="section-panel"></div>
  <h2 class="section-text">SECTION<br>HEADER</h2>
  <div class="footer-line"></div><div class="page-no">4</div>
</section>

<!-- Title only -->
<section class="slide" style="left:12px;top:600px">
  <div class="accent-bar"></div><h2 class="slide-title">TITLE GOES HERE</h2>
  <div class="brand"><span class="brand-mark"></span>Northvale</div>
  <div class="photo interior" style="left:0;top:24.7px;width:183px;height:135.3px" role="img" aria-label="Apartment kitchen with marble island and dining area"></div>
  <div class="photo tower" style="left:186px;top:24.7px;width:125px;height:135.3px" role="img" aria-label="Brick and glass apartment tower at street level"></div>
  <div class="footer-line"></div><div class="page-no">5</div>
</section>

<!-- Blank -->
<section class="slide" style="left:338px;top:600px">
  <div class="top-tab"></div>
  <div class="brand"><span class="brand-mark"></span>Northvale</div>
  <div class="footer-line"></div><div class="page-no">6</div>
</section>

<!-- Content with caption -->
<section class="slide" style="left:12px;top:791px">
  <div class="accent-bar"></div><h2 class="slide-title">TITLE GOES HERE</h2>
  <div class="brand"><span class="brand-mark"></span>Northvale</div>
  <div class="body" style="left:20.5px;top:29px;width:125px">
    <p>Lorem ipsum dolor sit amet, consectetuer adipiscing elit. Maecenas porttitor congue massa. Fusce posuere, magna sed pulvinar ultricies, purus lectus malesuada libero, sit amet commodo magna eros quis urna.</p>
    <p>Nunc viverra imperdiet enim. Fusce est. Vivamus a tellus.</p>
  </div>
  <div class="caption-line" style="left:20.5px;top:76px;width:124px"></div>
  <div class="caption" style="left:20.5px;top:78px">Lorem ipsum dolor sit</div>
  <div class="body" style="left:155px;top:29px;width:142px">
    <p>Lorem ipsum dolor sit amet, consectetuer adipiscing elit. Maecenas porttitor congue massa. Fusce posuere, magna sed pulvinar ultricies, purus lectus malesuada libero, sit amet commodo magna eros quis urna.</p>
    <p>Nunc viverra imperdiet enim. Fusce est. Vivamus a tellus.</p>
  </div>
  <div class="caption-line" style="left:155px;top:76px;width:141px"></div>
  <div class="caption" style="left:155px;top:78px">Lorem ipsum dolor sit</div>
  <div class="body" style="left:20.5px;top:98px;width:125px">
    <p>Lorem ipsum dolor sit amet, consectetuer adipiscing elit. Maecenas porttitor congue massa. Fusce posuere, magna sed pulvinar ultricies, purus lectus malesuada libero, sit amet commodo magna eros quis urna.</p>
    <p>Nunc viverra imperdiet enim. Fusce est. Vivamus a tellus.</p>
  </div>
  <div class="caption-line" style="left:20.5px;top:144.5px;width:124px"></div>
  <div class="caption" style="left:20.5px;top:146.5px">Lorem ipsum dolor sit</div>
  <div class="body" style="left:155px;top:98px;width:142px">
    <p>Lorem ipsum dolor sit amet, consectetuer adipiscing elit. Maecenas porttitor congue massa. Fusce posuere, magna sed pulvinar ultricies, purus lectus malesuada libero, sit amet commodo magna eros quis urna.</p>
    <p>Nunc viverra imperdiet enim. Fusce est. Vivamus a tellus.</p>
  </div>
  <div class="caption-line" style="left:155px;top:144.5px;width:141px"></div>
  <div class="caption" style="left:155px;top:146.5px">Lorem ipsum dolor sit</div>
  <div class="footer-line"></div><div class="page-no">7</div>
</section>

<!-- Picture grid with captions -->
<section class="slide" style="left:338px;top:791px">
  <div class="accent-bar"></div><h2 class="slide-title">TITLE GOES HERE</h2>
  <div class="brand"><span class="brand-mark"></span>Northvale</div>
  <div class="photo exterior" style="left:20.5px;top:31px;width:123.5px;height:50px" role="img" aria-label="Apartment complex at dusk"></div>
  <div class="caption-line" style="left:20.5px;top:84px;width:123.5px"></div>
  <div class="caption" style="left:20.5px;top:85.5px">Lorem ipsum dolor sit</div>
  <div class="photo exterior" style="left:164.5px;top:31px;width:123.5px;height:50px" role="img" aria-label="Apartment complex at dusk"></div>
  <div class="caption-line" style="left:164.5px;top:84px;width:123.5px"></div>
  <div class="caption" style="left:164.5px;top:85.5px">Lorem ipsum dolor sit</div>
  <div class="photo exterior" style="left:20.5px;top:99px;width:123.5px;height:50px" role="img" aria-label="Apartment complex at dusk"></div>
  <div class="caption-line" style="left:20.5px;top:152px;width:123.5px"></div>
  <div class="caption" style="left:20.5px;top:153.5px">Lorem ipsum dolor sit</div>
  <div class="photo exterior" style="left:164.5px;top:99px;width:123.5px;height:50px" role="img" aria-label="Apartment complex at dusk"></div>
  <div class="caption-line" style="left:164.5px;top:152px;width:123.5px"></div>
  <div class="caption" style="left:164.5px;top:153.5px">Lorem ipsum dolor sit</div>
  <div class="footer-line"></div><div class="page-no">8</div>
</section>

<!-- Picture with caption -->
<section class="slide" style="left:12px;top:981px">
  <div class="accent-bar"></div><h2 class="slide-title">TITLE GOES HERE</h2>
  <div class="brand"><span class="brand-mark"></span>Northvale</div>
  <div class="photo exterior" style="left:20.5px;top:30px;width:210px;height:85.5px" role="img" aria-label="Apartment complex at dusk with palm trees"></div>
  <div class="caption" style="left:236px;top:59px">Lorem ipsum dolor sit</div>
  <div class="photo exterior" style="left:193px;top:70px;width:104px;height:85px" role="img" aria-label="Close view of apartment entry with landscaping"></div>
  <div class="caption" style="left:23px;top:122px">Lorem ipsum dolor sit</div>
  <div class="footer-line"></div><div class="page-no">10</div>
</section>

<!-- Thank you -->
<section class="slide" style="left:338px;top:981px">
  <div class="thanks-panel"></div>
  <h2 class="thanks-text">THANK<br>YOU</h2>
  <div class="thanks-brand"><span class="brand-mark"></span>Northvale</div>
  <div class="footer-line thanks-line"></div><div class="page-no">10</div>
</section>

</body>
</html>
```